Logo & Visitenkarte für Soziale Dienstleistungen, Beratung & Therapie
Zielgruppe
[frontside]
Konrad Wallmuth
Dipl. Sozialpädagoge (FH)
systemischer Einzel-, Paar- und Familientherapeut (VKTB)
Mobil: 0176 / 4 829 31 57
Mail: konrad-wallmuth@rundpost.de
'Soziale Dienstleistungen, Beratung & Therapie' [slogan]
[social services, counseling & therapy]
'systemische Beratung & Therapie,
ambulante Hilfen zur Erziehung, intensive Familienberatung, aufsuchende Familientherapie
soziale Projekte, Erwachsenenbildung, Lehraufträge' [business offers - backside of the card]
Zielgruppen [traget groups]:
Familien, Kinder- und Jugendliche, Einzelpersonen, Netzwerkpartner,
Institutionen, Ämter, Schulen, Kliniken, etc.

```html
<!DOCTYPE html>
<html lang="de">
<head>
<meta charset="utf-8">
<title>Konrad Wallmuth – Corporate Design</title>
<link rel="stylesheet" href="https://fonts.googleapis.com/css2?family=Signika:wght@300;400;600&display=swap">
<style>
  :root {
    --teal: #137272;
    --teal-dark: #0f6464;
    --teal-mid: #2b8a84;
    --teal-grey: #9fbcb8;
    --teal-pale: #d3e5e3;
    --teal-faint: #e4efee;
    --green-soft: #7fb89a;
    --green-line: #5fa58c;
    --mint: #d8fdee;
    --ink: #5a5f63;
    --black: #000000;
    --white: #ffffff;
    --icon-grey: #4f7c78;
  }
  * { margin: 0; padding: 0; box-sizing: border-box; }
  html, body { width: 1200px; height: 2400px; overflow: hidden; background: var(--mint); }
  body { font-family: "Signika", sans-serif; color: var(--ink); }
  .board { position: relative; width: 1200px; height: 2400px; overflow: hidden; background: var(--mint); }

  .section-title { position: absolute; left: 60px; font-weight: 300; font-size: 33px; color: var(--ink); letter-spacing: 0.2px; }

  /* ---------- Logo & Icons ---------- */
  .logo-area { position: absolute; left: 0; top: 0; width: 1200px; height: 525px; background: var(--white); }
  .brand { position: absolute; }
  .brand .dot { position: absolute; border-radius: 50%; }
  .brand .name { position: absolute; font-weight: 600; white-space: nowrap; }
  .brand .tagline { position: absolute; font-weight: 300; white-space: nowrap; line-height: 1.3; }

  .brand--primary { left: 45px; top: 85px; width: 320px; height: 170px; }
  .brand--primary .dot { left: 10px; top: 55px; width: 56px; height: 56px; background: var(--teal); }
  .brand--primary .name { left: 81px; top: 28px; font-size: 23px; color: var(--ink); }
  .brand--primary .tagline { left: 81px; top: 80px; font-size: 22px; color: var(--ink); }

  .variant { position: absolute; display: flex; flex-direction: column; align-items: center; justify-content: center; gap: 10px; text-align: center; }
  .variant .dot { width: 34px; height: 34px; border-radius: 50%; }
  .variant .label { font-weight: 600; font-size: 17px; line-height: 1.15; }
  .v-teal   { left: 408px; top: 85px; width: 110px; height: 170px; color: var(--teal); }
  .v-teal .dot { background: var(--teal); }
  .v-pale   { left: 525px; top: 85px; width: 110px; height: 170px; color: var(--teal-pale); }
  .v-pale .dot { background: var(--teal-pale); }
  .v-black  { left: 640px; top: 85px; width: 110px; height: 170px; color: var(--black); }
  .v-black .dot { background: var(--black); }
  .v-box    { left: 752px; top: 75px; width: 119px; height: 198px; background: var(--teal); border-radius: 4px; color: var(--white); }
  .v-stairs { left: 925px; top: 60px; width: 225px; height: 170px; color: var(--teal-grey); }
  .v-stairs .dot { background: var(--teal); }
  .v-double { left: 45px; top: 305px; width: 215px; height: 175px; color: var(--teal); }
  .v-double .dot { background: var(--teal-grey); }
  .v-double-pale { left: 320px; top: 305px; width: 215px; height: 175px; color: var(--teal-pale); }
  .v-double-pale .dot { background: var(--teal-faint); }
  .v-twist { left: 610px; top: 305px; width: 120px; height: 175px; color: var(--teal); }
  .v-twist .dot { background: var(--teal-grey); }
  .v-twist-pale { left: 760px; top: 305px; width: 120px; height: 175px; color: var(--teal-pale); }
  .v-twist-pale .dot { background: var(--teal-faint); }

  .icon-set { position: absolute; left: 985px; top: 303px; width: 122px; height: 180px; }
  .icon-set svg { position: absolute; }

  /* ---------- Business Cards ---------- */
  .card { position: absolute; width: 150px; height: 231px; overflow: hidden; }
  .card--white { background: var(--white); }
  .card--black { background: var(--black); }
  .card-mark-teal { background: var(--teal); }
  .card-mark-black { background: var(--black); }

  /* pattern backs: soft tone fields, one per motif */
  .back-stairs-teal { background: linear-gradient(225deg, var(--teal) 0%, var(--teal) 30%, #3f9684 55%, var(--teal) 75%, var(--teal) 100%); }
  .back-grid-teal   { background: linear-gradient(180deg, #2e8679 0%, var(--teal) 25%, #2e8679 50%, var(--teal) 75%, #2e8679 100%); }
  .back-scatter-teal{ background: linear-gradient(135deg, #26807a 0%, var(--teal) 50%, #26807a 100%); }
  .back-twist-teal  { background: linear-gradient(90deg, var(--teal) 0%, #3a9184 20%, var(--teal) 40%, #3a9184 60%, var(--teal) 80%, #3a9184 100%); }
  .back-waves-teal  { background: radial-gradient(circle at 30% 30%, #3d9484 0%, var(--teal) 40%), radial-gradient(circle at 70% 75%, #3d9484 0%, transparent 40%); background-blend-mode: lighten; }
  .back-feature-teal{ background: radial-gradient(ellipse 45% 40% at 50% 55%, #6aae93 0%, #2b8a7d 55%, var(--teal) 100%); }

  .back-stairs-black { background: linear-gradient(225deg, #000 0%, #000 30%, #0d5a58 55%, #000 75%, #000 100%); }
  .back-grid-black   { background: linear-gradient(180deg, #0a3f3e 0%, #000 25%, #0a3f3e 50%, #000 75%, #0a3f3e 100%); }
  .back-scatter-black{ background: linear-gradient(135deg, #0a3a3a 0%, #000 50%, #0a3a3a 100%); }
  .back-twist-black  { background: linear-gradient(90deg, #000 0%, #0d5452 20%, #000 40%, #0d5452 60%, #000 80%, #0d5452 100%); }
  .back-waves-black  { background: radial-gradient(circle at 30% 30%, #0c4a49 0%, #000 45%), radial-gradient(circle at 70% 75%, #0c4a49 0%, transparent 40%); background-blend-mode: lighten; }
  .back-feature-black{ background: radial-gradient(ellipse 45% 40% at 50% 55%, #3f7f7a 0%, #0d4f4d 55%, #000 100%); }

  .card .dot { position: absolute; left: 14px; top: 18px; width: 22px; height: 22px; border-radius: 50%; background: var(--teal); }
  .card .name { position: absolute; left: 46px; top: 25px; font-size: 9px; font-weight: 400; white-space: nowrap; }
  .card .tagline { position: absolute; left: 46px; top: 46px; font-size: 8px; font-weight: 300; line-height: 1.4; white-space: nowrap; }
  .card .details { position: absolute; left: 14px; top: 140px; font-size: 6.2px; font-weight: 300; line-height: 1.45; white-space: nowrap; }
  .card .details strong { font-weight: 600; color: var(--teal); display: block; }
  .card .contact { position: absolute; left: 14px; top: 198px; font-size: 6.4px; font-weight: 300; line-height: 1.55; white-space: nowrap; }
  .card .contact span { display: flex; align-items: center; gap: 5px; }
  .card--white .name, .card--white .tagline, .card--white .details, .card--white .contact { color: #333; }
  .card--black .name, .card--black .tagline, .card--black .details, .card--black .contact { color: #e6e6e6; }
  .card--black .details strong { color: var(--teal-mid); }

  .card .mark-name { position: absolute; left: 0; right: 0; top: 50%; transform: translateY(-50%); text-align: center; font-size: 17px; font-weight: 600; line-height: 1.15; }
  .card .mark-name::before { content: ""; display: block; width: 30px; height: 30px; border-radius: 50%; margin: 0 auto 10px; background: currentColor; opacity: 0.55; }

  /* ---------- Letterhead ---------- */
  .sheet { position: absolute; width: 480px; height: 680px; background: var(--white); overflow: hidden; }
  .sheet--front { left: 60px; top: 1495px; z-index: 3; }
  .sheet--back  { left: 668px; top: 1455px; z-index: 1; }
  .sheet--tilted { left: 671px; top: 1575px; z-index: 2; transform-origin: 0 0; transform: rotate(28deg); box-shadow: 0 0 0 0.5px #e3ecea; }

  .sheet .dot { position: absolute; left: 34px; top: 44px; width: 42px; height: 42px; border-radius: 50%; background: var(--teal); }
  .sheet .name { position: absolute; left: 77px; top: 37px; font-size: 13.5px; color: #3e4346; white-space: nowrap; }
  .sheet .tagline { position: absolute; left: 77px; top: 70px; font-size: 12.5px; font-weight: 300; line-height: 1.35; color: #3e4346; white-space: nowrap; }
  .sheet .sidebar { position: absolute; left: 320px; top: 38px; font-size: 5.6px; font-weight: 300; line-height: 1.4; color: #555; white-space: nowrap; }
  .sheet .sidebar strong { display: block; font-weight: 600; color: var(--teal); }
  .sheet .sidebar .gap { display: block; height: 8px; }
  .sheet .body { position: absolute; left: 77px; top: 215px; width: 328px; font-size: 7.2px; font-weight: 300; line-height: 1.45; color: #444; text-align: justify; }
  .sheet .body p + p { margin-top: 9px; }
  .sheet .signature { position: absolute; left: 77px; top: 523px; font-size: 7.2px; font-weight: 300; line-height: 1.45; color: #444; }
  .sheet .signature strong { font-weight: 600; color: var(--teal); display: block; }
  .sheet .deco { position: absolute; left: 392px; top: 522px; width: 70px; height: 70px; border-radius: 50%; background: var(--teal-faint); }
  .sheet .footer { position: absolute; left: 77px; top: 641px; display: flex; gap: 22px; font-size: 5.6px; font-weight: 300; color: #555; line-height: 1.45; white-space: nowrap; }
  .sheet .footer .item { display: flex; gap: 5px; align-items: flex-start; }
  .sheet .footer .bank { border-left: 0.6px solid #999; padding-left: 8px; }
  .sheet--back .body { left: 170px; top: 210px; width: 260px; }
  .sheet--back .footer { left: 260px; top: 650px; }
</style>
</head>
<body>
<svg width="0" height="0" style="position:absolute" aria-hidden="true">
  <defs>
    <symbol id="icon-phone" viewBox="0 0 40 56">
      <rect x="3" y="3" width="34" height="50" rx="6" fill="none" stroke="currentColor" stroke-width="5"/>
      <g fill="currentColor">
        <circle cx="13" cy="26" r="2.2"/><circle cx="20" cy="26" r="2.2"/><circle cx="27" cy="26" r="2.2"/>
        <circle cx="13" cy="33" r="2.2"/><circle cx="20" cy="33" r="2.2"/><circle cx="27" cy="33" r="2.2"/>
        <circle cx="13" cy="40" r="2.2"/><circle cx="20" cy="40" r="2.2"/><circle cx="27" cy="40" r="2.2"/>
      </g>
    </symbol>
    <symbol id="icon-mail" viewBox="0 0 54 40">
      <rect x="3" y="3" width="48" height="34" rx="5" fill="none" stroke="currentColor" stroke-width="5"/>
      <path d="M11 12 L27 22 L43 12" fill="none" stroke="currentColor" stroke-width="5" stroke-linecap="round" stroke-linejoin="round"/>
    </symbol>
    <symbol id="icon-pin" viewBox="0 0 44 60">
      <path d="M22 56 C14 44 4 33 4 22 A18 18 0 0 1 40 22 C40 33 30 44 22 56 Z" fill="none" stroke="currentColor" stroke-width="5" stroke-linejoin="round"/>
      <circle cx="22" cy="22" r="7" fill="none" stroke="currentColor" stroke-width="5"/>
    </symbol>
  </defs>
</svg>

<main class="board">

  <!-- Logo & Icons -->
  <section class="logo-area">
    <h2 class="section-title" style="top:18px;">Logo &amp; Icons</h2>

    <div class="brand brand--primary">
      <span class="dot"></span>
      <span class="name">Konrad Wallmuth</span>
      <span class="tagline">Soziale Dienstleistungen,<br>Beratung &amp; Therapie</span>
    </div>

    <div class="variant v-teal"><span class="dot"></span><span class="label">Konrad<br>Wallmuth</span></div>
    <div class="variant v-pale"><span class="dot"></span><span class="label">Konrad<br>Wallmuth</span></div>
    <div class="variant v-black"><span class="dot"></span><span class="label">Konrad<br>Wallmuth</span></div>
    <div class="variant v-box"><span class="label">Konrad<br>Wallmuth</span></div>
    <div class="variant v-stairs"><span class="dot"></span><span class="label">Konrad Wallmuth</span></div>

    <div class="variant v-double"><span class="dot"></span><span class="label">Konrad<br>Wallmuth</span></div>
    <div class="variant v-double-pale"><span class="dot"></span><span class="label">Konrad<br>Wallmuth</span></div>
    <div class="variant v-twist"><span class="dot"></span><span class="label">Konrad<br>Wallmuth</span></div>
    <div class="variant v-twist-pale"><span class="dot"></span><span class="label">Konrad<br>Wallmuth</span></div>

    <div class="icon-set">
      <svg style="left:6px;top:0;color:var(--teal)" width="38" height="53"><use href="#icon-phone"/></svg>
      <svg style="left:72px;top:0;color:var(--icon-grey)" width="38" height="53"><use href="#icon-phone"/></svg>
      <svg style="left:0;top:67px;color:var(--teal)" width="52" height="39"><use href="#icon-mail"/></svg>
      <svg style="left:66px;top:67px;color:var(--icon-grey)" width="52" height="39"><use href="#icon-mail"/></svg>
      <svg style="left:6px;top:120px;color:var(--teal)" width="42" height="58"><use href="#icon-pin"/></svg>
      <svg style="left:70px;top:120px;color:var(--icon-grey)" width="42" height="58"><use href="#icon-pin"/></svg>
    </div>
  </section>

  <!-- Business Cards -->
  <h2 class="section-title" style="top:542px;">Business Cards</h2>

  <article class="card card--white" style="left:60px;top:620px;">
    <span class="dot"></span>
    <span class="name">Konrad Wallmuth</span>
    <span class="tagline">Soziale Dienstleistungen,<br>Beratung &amp; Therapie</span>
    <div class="details"><strong>Konrad Wallmuth</strong>Dipl. Sozialpädagoge (FH)<br>systemischer Berater (VKTB)<br>systemischer Einzel-, Paar-<br>&amp; Familientherapeut (VKTB)</div>
    <div class="contact">
      <span><svg width="6" height="8" style="color:var(--teal)"><use href="#icon-phone"/></svg>0176 / 4 829 31 57</span>
      <span><svg width="8" height="6" style="color:var(--teal)"><use href="#icon-mail"/></svg>konrad-wallmuth@rundpost.de</span>
    </div>
  </article>
  <div class="card back-stairs-teal" style="left:231px;top:620px;" role="img" aria-label="Kartenrückseite: diagonales Stufenmuster aus hellgrünen Linien auf Petrol"></div>
  <div class="card back-grid-teal" style="left:403px;top:620px;" role="img" aria-label="Kartenrückseite: Raster aus hellgrünen Rahmenformen auf Petrol"></div>

  <article class="card card--black" style="left:643px;top:620px;">
    <span class="dot"></span>
    <span class="name">Konrad Wallmuth</span>
    <span class="tagline">Soziale Dienstleistungen,<br>Beratung &amp; Therapie</span>
    <div class="details"><strong>Konrad Wallmuth</strong>Dipl. Sozialpädagoge (FH)<br>systemischer Berater (VKTB)<br>systemischer Einzel-, Paar-<br>&amp; Familientherapeut (VKTB)</div>
    <div class="contact">
      <span><svg width="6" height="8" style="color:var(--teal)"><use href="#icon-phone"/></svg>0176 / 4 829 31 57</span>
      <span><svg width="8" height="6" style="color:var(--teal)"><use href="#icon-mail"/></svg>konrad-wallmuth@rundpost.de</span>
    </div>
  </article>
  <div class="card back-stairs-black" style="left:814px;top:620px;" role="img" aria-label="Kartenrückseite: diagonales Stufenmuster aus Petrol-Linien auf Schwarz"></div>
  <div class="card back-grid-black" style="left:986px;top:620px;" role="img" aria-label="Kartenrückseite: Raster aus Petrol-Rahmenformen auf Schwarz"></div>

  <div class="card back-scatter-teal" style="left:60px;top:872px;" role="img" aria-label="Kartenrückseite: versetztes Streumuster aus Linienformen auf Petrol"></div>
  <div class="card back-twist-teal" style="left:231px;top:872px;" role="img" aria-label="Kartenrückseite: Reihen verschlungener Linien auf Petrol"></div>
  <div class="card back-waves-teal" style="left:403px;top:872px;" role="img" aria-label="Kartenrückseite: freies Muster geschwungener Linien auf Petrol"></div>
  <div class="card back-scatter-black" style="left:643px;top:872px;" role="img" aria-label="Kartenrückseite: versetztes Streumuster aus Linienformen auf Schwarz"></div>
  <div class="card back-twist-black" style="left:814px;top:872px;" role="img" aria-label="Kartenrückseite: Reihen verschlungener Linien auf Schwarz"></div>
  <div class="card back-waves-black" style="left:986px;top:872px;" role="img" aria-label="Kartenrückseite: freies Muster geschwungener Linien auf Schwarz"></div>

  <div class="card back-feature-teal" style="left:60px;top:1125px;" role="img" aria-label="Kartenrückseite: Linienmuster mit großer hellgrüner Schmuckform auf Petrol"></div>
  <div class="card card-mark-teal" style="left:231px;top:1125px;"><span class="mark-name" style="color:var(--green-soft);">Konrad<br>Wallmuth</span></div>
  <div class="card card-mark-teal" style="left:403px;top:1125px;"><span class="mark-name" style="color:var(--green-soft);">Konrad<br>Wallmuth</span></div>
  <div class="card back-feature-black" style="left:643px;top:1125px;" role="img" aria-label="Kartenrückseite: Linienmuster mit großer Petrol-Schmuckform auf Schwarz"></div>
  <div class="card card-mark-black" style="left:814px;top:1125px;"><span class="mark-name" style="color:var(--teal-mid);">Konrad<br>Wallmuth</span></div>
  <div class="card card-mark-black" style="left:986px;top:1125px;"><span class="mark-name" style="color:var(--teal-mid);">Konrad<br>Wallmuth</span></div>

  <!-- Letterhead -->
  <h2 class="section-title" style="top:1416px;">Letterhead</h2>

  <article class="sheet sheet--back">
    <span class="dot" style="background:var(--teal-grey);"></span>
    <span class="name">Konrad Wallmuth</span>
    <span class="tagline">Soziale Dienstleistungen,<br>Beratung &amp; Therapie</span>
    <div class="sidebar"><strong>Konrad Wallmuth</strong>Dipl. Sozialpädagoge (FH)<br>systemischer Berater (VKTB)<br>systemischer Einzel-, Paar-<br>&amp; Familientherapeut (VKTB)<span class="gap"></span>Kinderschutzfachkraft<br>(gem. § 8a/b SGB VIII &amp; § 4 KKG)</div>
    <div class="body">
      <p>Lorem ipsum dolor sit amet, consectetur adipiscing elit. Integer pharetra erat quis metus bibendum condimentum. Ut non justo velit. Ut eu porttitor dui. Phasellus nec suscipit mauris. Curabitur fringilla ante ac libero pretium porta. Aenean tristique non massa at pretium. Phasellus nec pulvinar erat. Vivamus accumsan risus nisi, vel blandit nisi maximus in. Etiam placerat feugiat sem vitae aliquam. Praesent fermentum elementum blandit. Duis magna velit, dignissim a felis sit amet, faucibus eleifend neque.</p>
      <p>Mauris lobortis tincidunt ultricies. Curabitur tempor magna est, eget congue metus faucibus at. Curabitur id libero quis mi pretium semper ut sed lectus. Morbi non lobortis orci. Lorem ipsum dolor sit amet, consectetur adipiscing elit.</p>
    </div>
    <div class="deco"></div>
    <div class="footer">
      <div class="item bank">Bank details: XXXXX-XXXX-XXXXX<br>Tax ID: &nbsp;&nbsp;&nbsp;&nbsp;&nbsp;XXXXXXXX</div>
    </div>
  </article>

  <article class="sheet sheet--tilted">
    <span class="dot" style="background:var(--teal-grey);"></span>
    <span class="name">Konrad Wallmuth</span>
    <span class="tagline">Soziale Dienstleistungen,<br>Beratung &amp; Therapie</span>
    <div class="sidebar" style="top:92px;"><strong>Konrad Wallmuth</strong>Dipl. Sozialpädagoge (FH)<br>systemischer Berater (VKTB)<br>systemischer Einzel-, Paar-<br>&amp; Familientherapeut (VKTB)<span class="gap"></span>Kinderschutzfachkraft<br>(gem. § 8a/b SGB VIII &amp; § 4 KKG)</div>
    <div class="body">
      <p>Lorem ipsum dolor sit amet, consectetur adipiscing elit. Integer pharetra erat quis metus bibendum condimentum. Ut non justo velit. Ut eu porttitor dui. Phasellus nec suscipit mauris. Curabitur fringilla ante ac libero pretium porta. Aenean tristique non massa at pretium. Phasellus nec pulvinar erat. Vivamus accumsan risus nisi, vel blandit nisi maximus in. Donec ut lacus sagittis, consequat augue et, placerat ex. Etiam placerat feugiat sem vitae aliquam. Praesent finibus risus a sem mattis, vitae blandit sem tincidunt. Praesent fermentum elementum blandit. Duis magna velit, dignissim a felis sit amet, faucibus eleifend neque. Sed elementum neque lectus, eu pharetra tellus iaculis ac.</p>
      <p>Mauris lobortis tincidunt ultricies. Curabitur tempor magna est, eget congue metus faucibus at. Curabitur id libero quis mi pretium semper ut sed lectus. Morbi non lobortis orci. Lorem ipsum dolor sit amet, consectetur adipiscing elit. Nam urna dolor, scelerisque a venenatis non, interdum vitae mi. Mauris hendrerit odio at arcu suscipit molestie. Curabitur risus ex, pretium a felis vitae, viverra vestibulum leo. Phasellus pharetra, lorem non pellentesque semper, neque lacus lobortis metus, id sagittis velit augue sit amet justo.</p>
      <p>Proin sed faucibus risus. Vivamus sed vehicula lorem, ac finibus nulla. Orci varius natoque penatibus et magnis dis parturient montes, nascetur ridiculus mus. Mauris pulvinar erat ut viverra laoreet. Maecenas fermentum ornare massa in eleifend. Sed efficitur dui a tortor vulputate accumsan. Suspendisse facilisis, nisi nec consequat laoreet, ante diam pulvinar ex, a tincidunt ex eros id ligula. Vestibulum vestibulum efficitur aliquet. Sed lobortis velit eget risus aliquet volutpat. Aliquam nibh erat, lobortis vel ligula et, ultricies suscipit mi.</p>
    </div>
    <div class="signature"><strong>Konrad Wallmuth</strong>Dipl. Sozialpädagoge (FH) systemischer Einzel-,<br>Paar- und Familientherapeut (VKTB)</div>
    <div class="deco" style="left:250px;top:560px;width:90px;height:90px;"></div>
    <div class="footer">
      <div class="item"><svg width="6" height="8" style="color:var(--teal)"><use href="#icon-pin"/></svg><span>Street address<br>City, State, Zip</span></div>
      <div class="item"><svg width="6" height="8" style="color:var(--teal)"><use href="#icon-phone"/></svg><span>0176 / 4 829 31 57<br>konrad-wallmuth@rundpost.de</span></div>
      <div class="item bank">Bank details: XXXXX-XXXX-XXXXX<br>Tax ID: &nbsp;&nbsp;&nbsp;&nbsp;&nbsp;XXXXXXXX</div>
    </div>
  </article>

  <article class="sheet sheet--front">
    <span class="dot"></span>
    <span class="name">Konrad Wallmuth</span>
    <span class="tagline">Soziale Dienstleistungen,<br>Beratung &amp; Therapie</span>
    <div class="sidebar"><strong>Konrad Wallmuth</strong>Dipl. Sozialpädagoge (FH)<br>systemischer Berater (VKTB)<br>systemischer Einzel-, Paar-<br>&amp; Familientherapeut (VKTB)<span class="gap"></span>Kinderschutzfachkraft<br>(gem. § 8a/b SGB VIII &amp; § 4 KKG)</div>
    <div class="body">
      <p>Lorem ipsum dolor sit amet, consectetur adipiscing elit. Integer pharetra erat quis metus bibendum condimentum. Ut non justo velit. Ut eu porttitor dui. Phasellus nec suscipit mauris. Curabitur fringilla ante ac libero pretium porta. Aenean tristique non massa at pretium. Phasellus nec pulvinar erat. Vivamus accumsan risus nisi, vel blandit nisi maximus in. Donec ut lacus sagittis, consequat augue et, placerat ex. Etiam placerat feugiat sem vitae aliquam. Praesent finibus risus a sem mattis, vitae blandit sem tincidunt. Praesent fermentum elementum blandit. Duis magna velit, dignissim a felis sit amet, faucibus eleifend neque. Sed elementum neque lectus, eu pharetra tellus iaculis ac.</p>
      <p>Mauris lobortis tincidunt ultricies. Curabitur tempor magna est, eget congue metus faucibus at. Curabitur id libero quis mi pretium semper ut sed lectus. Morbi non lobortis orci. Lorem ipsum dolor sit amet, consectetur adipiscing elit. Nam urna dolor, scelerisque a venenatis non, interdum vitae mi. Mauris hendrerit odio at arcu suscipit molestie. Curabitur risus ex, pretium a felis vitae, viverra vestibulum leo. Phasellus pharetra, lorem non pellentesque semper, neque lacus lobortis metus, id sagittis velit augue sit amet justo.</p>
      <p>Proin sed faucibus risus. Vivamus sed vehicula lorem, ac finibus nulla. Orci varius natoque penatibus et magnis dis parturient montes, nascetur ridiculus mus. Mauris pulvinar erat ut viverra laoreet. Maecenas fermentum ornare massa in eleifend. Sed efficitur dui a tortor vulputate accumsan. Suspendisse facilisis, nisi nec consequat laoreet, ante diam pulvinar ex, a tincidunt ex eros id ligula. Vestibulum vestibulum efficitur aliquet. Sed lobortis velit eget risus aliquet volutpat. Aliquam nibh erat, lobortis vel ligula et, ultricies suscipit mi.</p>
    </div>
    <div class="signature"><strong>Konrad Wallmuth</strong>Dipl. Sozialpädagoge (FH) systemischer Einzel-,<br>Paar- und Familientherapeut (VKTB)</div>
    <div class="deco"></div>
    <div class="footer">
      <div class="item"><svg width="6" height="8" style="color:var(--teal)"><use href="#icon-pin"/></svg><span>Street address<br>City, State, Zip</span></div>
      <div class="item"><svg width="6" height="8" style="color:var(--teal)"><use href="#icon-phone"/></svg><span>0176 / 4 829 31 57<br>konrad-wallmuth@rundpost.de</span></div>
      <div class="item bank">Bank details: XXXXX-XXXX-XXXXX<br>Tax ID: &nbsp;&nbsp;&nbsp;&nbsp;&nbsp;XXXXXXXX</div>
    </div>
  </article>

</main>
</body>
</html>
```